A book cover for an ESL self-study guide to English small talk with exercises and answers

I need a book cover for an ESL self-study guide to English small talk with exercises. It has useful phrases, idioms, and vocabulary in it but I will provide the blub for the back of the book. I would like a simple design. I had the idea to use a red background and the letters 'English' being large across the front in Union Jack lettering then 'ESL' below in different lettering and Small talk further down. I am not sure if the Union Jack lettering will stand out well enough on a red background so we might have to use a different background or edging for those letters but Ideally, I'd like the book to be red and either the 'ESL' or 'Small Talk' to be a vivid blue but again if something else looks better go with it. If it looks like this design idea doesn't work I am open to other ideas too. If the Union Jack lettering is not used I will need a Union Jack on there somewhere to show that the book is in British English. Those are my ideas but ultimately, you guys are the professionals.

Target Market(s)

People who are learning English from ESL students to professionals. I expect the market to be more professionals.

Industry/Entity Type

Education.

Colors
EB3D1F
EC4F4E
F09395
F8D3D4
FCEDEE

Requirements
Must have
• A Union Jack or union jack lettering to show the book is in British English. I would like to cover to be striking and stand out from the others in it's genre without being gaudy.
Nice to have
• I would like the cover to be red but ultimately you guys are the professionals and I'm sure you know more than I do. Scripts should be easy to read as it's for ESL students.

```html
<!DOCTYPE html>
<html lang="en">
<head>
<meta charset="UTF-8">
<title>English ESL – Small Talk</title>
<link rel="stylesheet" href="https://fonts.googleapis.com/css2?family=Bebas+Neue&family=Libre+Baskerville:wght@700&family=Montserrat:wght@800&display=swap">
<style>
  :root {
    --cover-red: #d00522;
    --flag-blue: #1b2a7a;
    --flag-red: #d8152e;
    --flag-white: #f4f1f1;
    --label-blue: #14238a;
    --text-white: #ffffff;
    --bubble-white: #ffffff;
  }
  html, body {
    margin: 0;
    padding: 0;
    overflow: hidden;
    background: var(--cover-red);
  }
  .cover {
    position: relative;
    width: 750px;
    height: 1200px;
    overflow: hidden;
    background: var(--cover-red);
  }
  .flag-banner {
    position: absolute;
    top: 0;
    left: 0;
    width: 750px;
    height: 350px;
  }
  .title {
    position: absolute;
    top: 380px;
    left: 0;
    width: 750px;
    height: 230px;
  }
  .title text {
    font-family: "Bebas Neue", "Oswald", sans-serif;
    fill: var(--text-white);
  }
  .series-label {
    position: absolute;
    top: 640px;
    left: 198px;
    width: 360px;
    height: 102px;
    background: var(--label-blue);
    display: flex;
    align-items: center;
    justify-content: center;
    color: var(--text-white);
    font-family: "Libre Baskerville", "Times New Roman", serif;
    font-weight: 700;
    font-size: 58px;
    letter-spacing: 28px;
    padding-left: 28px;
    box-sizing: border-box;
    line-height: 1;
  }
  .subtitle-bubble {
    position: absolute;
    top: 866px;
    left: 168px;
    width: 416px;
    height: 186px;
  }
  .subtitle-bubble text {
    font-family: "Montserrat", "Arial", sans-serif;
    font-weight: 800;
    fill: var(--label-blue);
  }
</style>
</head>
<body>
<main class="cover">
  <svg class="flag-banner" viewBox="0 0 750 350" role="img" aria-label="Photograph of a waving Union Jack flag draped across the top of the cover">
    <defs>
      <linearGradient id="flagTones" x1="0" y1="0" x2="1" y2="0.6">
        <stop offset="0" stop-color="var(--flag-blue)"/>
        <stop offset="0.18" stop-color="var(--flag-white)"/>
        <stop offset="0.36" stop-color="var(--flag-red)"/>
        <stop offset="0.55" stop-color="var(--flag-white)"/>
        <stop offset="0.72" stop-color="var(--flag-blue)"/>
        <stop offset="0.86" stop-color="var(--flag-red)"/>
        <stop offset="1" stop-color="var(--flag-blue)"/>
      </linearGradient>
    </defs>
    <path d="M0 0 H750 V236 C720 228 700 218 680 224 C650 236 620 270 560 310 C540 326 530 334 520 330 C490 300 470 270 420 262 C370 254 320 250 260 240 C180 230 90 238 0 236 Z" fill="url(#flagTones)"/>
  </svg>

  <svg class="title" viewBox="0 0 750 230">
    <text x="62" y="212" font-size="274" textLength="628" lengthAdjust="spacingAndGlyphs">ENGLISH</text>
  </svg>

  <div class="series-label">ESL</div>

  <svg class="subtitle-bubble" viewBox="0 0 416 186">
    <path class="bubble-shape" d="M208 4 C322 4 412 40 412 82 C412 118 352 148 280 158 C290 168 296 174 308 180 C284 182 262 174 246 162 C234 162 222 162 208 162 C94 162 4 126 4 82 C4 40 94 4 208 4 Z" fill="var(--bubble-white)"/>
    <text x="208" y="101" font-size="66" text-anchor="middle" textLength="316" lengthAdjust="spacingAndGlyphs">Small Talk</text>
  </svg>
</main>
</body>
</html>
```